Wine Lable

We Are Marlowby Ridge Wines and we are designing a new bottle for our top end wine named "The Velvet Bramble" I no exactly how i want the label to look and im searching for a talented designer to out my vision to life.

There will be 3 parts to this design.

Top Cover design with gold text wrapped around saying"The Velvet Bramble" (See Fig 2)

The front label which i want same as attached (See fig 2)

The Rear label
(See Fig 2 for design)
(See Fig 3 for content)

and final bottle design how it will look together

Come on guys keep the designs coming

Reason: I have extended my deadline due to the break from work over the Christmas new year period. Extra consideration will be made

Target Market(s)

The High End wine consumers the bottle cost will be $100USD

Font styles to use
Decorative
Script

Requirements
Must have

• Top Cover design with gold text wrapped around saying"The Velvet Bramble" (See Fig 2)
Black Rear Label with information and company name (Layout Fig 2) (Content Fig 3)
Gold and Black theme
The Text "Wine of Australia" somewhere on the bottle

```html
<!DOCTYPE html>
<html lang="en">
<head>
<meta charset="utf-8">
<title>The Velvet Bramble – Label Set</title>
<link rel="stylesheet" href="https://fonts.googleapis.com/css2?family=Yesteryear&family=Old+Standard+TT:ital,wght@0,400;0,700;1,400&display=swap">
<style>
  :root {
    --ink: #050505;
    --gold-deep: #8a5a0e;
    --gold: #c9941f;
    --gold-light: #f6d772;
    --gold-shine: linear-gradient(100deg, #8a5a0e 0%, #e0b040 22%, #f8df84 42%, #c9941f 62%, #f1cd62 82%, #8a5a0e 100%);
    --backdrop: #d8d6d3;
    --script: "Yesteryear", cursive;
    --serif: "Old Standard TT", serif;
  }
  * { box-sizing: border-box; margin: 0; padding: 0; }
  html, body { width: 950px; height: 1200px; overflow: hidden; }
  body {
    background: var(--backdrop);
    position: relative;
    font-family: var(--serif);
  }

  /* Neck capsule band */
  .neck-band {
    position: absolute; left: 225px; top: 60px;
    width: 500px; height: 92px;
    background: var(--ink);
  }
  .neck-band__title {
    height: 50px; display: flex; align-items: center; justify-content: center;
    font-family: var(--script); font-size: 38px; color: var(--gold-light);
  }
  .neck-band__rule { height: 3px; background: var(--gold-shine); }
  .neck-band__ornament {
    height: 30px; margin: 3px 0;
    background: repeating-linear-gradient(90deg, var(--gold) 0 14px, var(--ink) 14px 20px, var(--gold-light) 20px 30px, var(--ink) 30px 36px);
  }

  /* Front label */
  .front-label {
    position: absolute; left: 60px; top: 200px;
    width: 450px; height: 800px;
    background: var(--ink);
    border: 5px solid var(--gold);
    outline: 2px solid var(--gold-light); outline-offset: -12px;
  }
  .front-label__pattern {
    position: absolute; left: 18px; right: 18px; top: 18px; bottom: 58px;
    background:
      radial-gradient(circle at 30% 25%, rgba(248,223,132,.55), transparent 40%),
      radial-gradient(circle at 70% 65%, rgba(201,148,31,.55), transparent 45%),
      linear-gradient(160deg, #3a2606 0%, #7a5210 45%, #2a1b04 100%);
  }
  .front-label__title {
    position: absolute; left: 0; right: 0; top: 165px;
    text-align: center;
    font-family: var(--script); font-size: 72px; line-height: 1;
    color: var(--gold-light);
  }
  .front-label__origin {
    position: absolute; left: 0; right: 0; bottom: 18px;
    text-align: center; font-size: 22px; color: var(--gold);
  }

  /* Rear label */
  .rear-label {
    position: absolute; left: 570px; top: 200px;
    width: 320px; height: 800px;
    background: var(--ink);
    border: 4px solid var(--gold);
    padding: 8px;
    display: flex; flex-direction: column; gap: 6px;
  }
  .rear-label__crest-panel {
    height: 190px; background: var(--gold-shine);
    display: flex; align-items: center; justify-content: center;
  }
  .rear-label__crest {
    width: 150px; height: 150px;
    border: 3px solid var(--ink);
    background: radial-gradient(circle at 45% 40%, #d7a73a 0%, #6b470c 55%, #1a1003 100%);
  }
  .rear-label__ornament {
    height: 30px;
    background: repeating-linear-gradient(90deg, var(--gold) 0 12px, var(--ink) 12px 18px, var(--gold-light) 18px 28px, var(--ink) 28px 34px);
  }
  .rear-label__story {
    background: var(--gold-shine);
    padding: 12px 18px 16px;
    color: #2a1a03;
  }
  .rear-label__winery {
    text-align: center; font-size: 15px; letter-spacing: .5px;
    text-transform: uppercase; margin-bottom: 6px;
  }
  .rear-label__notes {
    font-size: 13.5px; line-height: 1.32; text-align: justify;
  }
  .rear-label__facts {
    flex: 1; border: 2px solid var(--gold);
    padding: 12px 16px; color: var(--gold-light);
    position: relative;
  }
  .facts__row { display: flex; justify-content: space-between; font-size: 13px; }
  .facts__big { font-size: 30px; line-height: 1.1; }
  .facts__drinks { margin-top: 8px; font-size: 13px; }
  .facts__drinks strong { font-size: 26px; font-weight: 400; margin-left: 4px; }
  .facts__sulphites { font-style: italic; font-size: 12px; }
  .facts__origin { margin-top: 16px; font-size: 15px; }
  .facts__producer { margin-top: 14px; font-size: 12px; line-height: 1.3; width: 150px; }
  .facts__map {
    position: absolute; right: 16px; bottom: 36px;
    width: 110px; height: 100px;
    background: linear-gradient(135deg, var(--gold-light), var(--gold-deep));
    border-radius: 40% 55% 45% 50%;
  }
</style>
</head>
<body>

  <section class="neck-band" aria-label="Neck capsule band">
    <div class="neck-band__title">The Velvet Bramble</div>
    <div class="neck-band__rule"></div>
    <div class="neck-band__ornament" role="img" aria-label="Gold scrolling vine border"></div>
    <div class="neck-band__rule"></div>
  </section>

  <section class="front-label" aria-label="Front label">
    <div class="front-label__pattern" role="img" aria-label="Gold vine leaves and grape clusters pattern on black"></div>
    <h1 class="front-label__title">The Velvet Bramble</h1>
    <p class="front-label__origin">Wine of Australia</p>
  </section>

  <section class="rear-label" aria-label="Rear label">
    <div class="rear-label__crest-panel">
      <div class="rear-label__crest" role="img" aria-label="Gold vine leaf and grape ornament on black"></div>
    </div>
    <div class="rear-label__ornament" role="img" aria-label="Gold scrolling vine border"></div>
    <div class="rear-label__story">
      <h2 class="rear-label__winery">Marlowby Ridge Wines</h2>
      <p class="rear-label__notes">Deep, vibrant crimson/garnet colour. Blackcurrant and plum aromas with lifted clove-like spice complemented by toasty oak and a touch of fennel. Intense but balanced juicy red currant and plum characters on the palate with a gentle spice. Generous, soft mouth-filling tannins and balanced acidity.</p>
    </div>
    <div class="rear-label__facts">
      <div class="facts__row"><span>Net Content</span><span>Alcohol Strength</span></div>
      <div class="facts__row facts__big"><span>750ml</span><span>15.5%</span></div>
      <div class="facts__row facts__drinks">
        <span>Approx<strong>9.1</strong><br>Standard Drinks</span>
        <span class="facts__sulphites">Contains Sulphites</span>
      </div>
      <p class="facts__origin">Wine of Australia</p>
      <p class="facts__producer">Produced by:<br>Copper Finch Australia<br>Unit 3<br>212 Hollow Creek Road<br>Westbury 5099<br>South Australia, Australia</p>
      <div class="facts__map" role="img" aria-label="Gold map of Australia"></div>
    </div>
  </section>

</body>
</html>
```